Plumbing Business needs a more appealing business card design and logo

card must include phone number and logo, open to new logo ideas, full creative freedom

Industry/Entity Type

Plumbing

Contact Information for Business Card

Darrell Whitcombe
0417305829

Logo Text

call outs from $80

Font styles to use
• unsure

Colors
ec1f27
0255a3
f78f20

```html
<!DOCTYPE html>
<html lang="en">
<head>
<meta charset="utf-8">
<title>Halvorsen Plumbing — Business Card</title>
<link href="https://fonts.googleapis.com/css2?family=Lato:wght@400;700;900&display=swap" rel="stylesheet">
<style>
  :root {
    --backdrop: #5b5b5b;
    --blue-deep: #0456ad;
    --blue-mid: #0a62c4;
    --blue-bright: #1a86ea;
    --blue-light: #2a8fe8;
    --ink: #1f1f1f;
    --paper: #ffffff;
  }
  * { margin: 0; padding: 0; box-sizing: border-box; }
  html, body {
    width: 1200px; height: 802px; overflow: hidden;
    background: var(--backdrop);
    font-family: "Lato", sans-serif;
  }
  .card {
    position: absolute; top: 274px;
    width: 442px; height: 264px;
    overflow: hidden;
    box-shadow: 0 4px 10px rgba(0,0,0,0.45);
  }
  /* Front */
  .card-front { left: 136px; background: var(--paper); }
  .card-front .band {
    position: absolute; left: 0; top: 0; bottom: 0; width: 48px;
    background: var(--blue-mid);
  }
  .card-front .band-accent {
    position: absolute; left: 48px; top: 0; bottom: 0; width: 4px;
    background: var(--blue-bright);
  }
  .brand-front {
    position: absolute; right: 30px; top: 40px;
    display: flex; flex-direction: column; align-items: center; gap: 10px;
  }
  .brand-dot {
    width: 46px; height: 46px; border-radius: 50%;
    background: var(--blue-mid);
  }
  .brand-name {
    font-weight: 900; font-size: 19px; letter-spacing: 0.2px;
    color: var(--blue-mid); text-transform: uppercase; white-space: nowrap;
  }
  .person {
    position: absolute; left: 72px; top: 160px;
    font-size: 18px; font-weight: 400; text-transform: uppercase;
    color: var(--blue-light); white-space: nowrap;
  }
  .person .surname { color: var(--blue-mid); font-weight: 700; }
  .contacts {
    position: absolute; left: 72px; top: 198px;
    list-style: none; font-size: 12.5px; color: var(--ink); line-height: 16px;
  }
  .contacts li { display: flex; align-items: center; gap: 5px; }
  .contacts svg { width: 10px; height: 10px; flex: none; fill: var(--blue-mid); }
  /* Back */
  .card-back {
    left: 624px;
    background: radial-gradient(ellipse 60% 70% at 50% 35%, #1f8ae6 0%, var(--blue-mid) 55%, var(--blue-deep) 100%);
    color: var(--paper);
  }
  .brand-back {
    position: absolute; left: 0; right: 0; top: 86px;
    display: flex; align-items: center; justify-content: center; gap: 14px;
  }
  .brand-back .brand-dot { width: 58px; height: 58px; background: var(--paper); }
  .brand-back .brand-name { color: var(--paper); font-size: 28px; }
  .web-back {
    position: absolute; left: 0; right: 0; top: 224px;
    text-align: center; font-size: 12.5px;
  }
</style>
</head>
<body>
  <section class="card card-front">
    <div class="band"></div>
    <div class="band-accent"></div>
    <div class="brand-front">
      <div class="brand-dot"></div>
      <div class="brand-name">Halvorsen Plumbing</div>
    </div>
    <h1 class="person">Darrell <span class="surname">Whitcombe</span></h1>
    <ul class="contacts">
      <li>
        <svg viewBox="0 0 10 10" aria-hidden="true"><path d="M1 3 Q5 0 9 3 L8 4.5 L6.5 3.8 L6.5 3 Q5 2.5 3.5 3 L3.5 3.8 L2 4.5 Z M2 5.5 H8 V9 H2 Z"/></svg>
        0417305829
      </li>
      <li>
        <svg viewBox="0 0 10 10" aria-hidden="true"><path d="M0.5 2 H9.5 V8.5 H0.5 Z M1 2.5 L5 5.5 L9 2.5" fill="none" stroke="#0a62c4" stroke-width="1.2"/></svg>
        info@halvorsenplumbing.com
      </li>
      <li>
        <svg viewBox="0 0 10 10" aria-hidden="true"><circle cx="5" cy="5" r="4.5"/></svg>
        www.halvorsenplumbing.com
      </li>
    </ul>
  </section>

  <section class="card card-back">
    <div class="brand-back">
      <div class="brand-dot"></div>
      <div class="brand-name">Halvorsen Plumbing</div>
    </div>
    <div class="web-back">www.halvorsenplumbing.com</div>
  </section>
</body>
</html>
```